Looking for business card/letterhead/email signature

Take existing logo and create full design suite of collateral

Contact Information for Business Card

Use mock details that can be edited by us

Font styles to use
Sans Serif

```html
<!DOCTYPE html>
<html lang="en">
<head>
<meta charset="utf-8">
<title>Harlow Digital Letterhead</title>
<link rel="stylesheet" href="https://fonts.googleapis.com/css2?family=Open+Sans:wght@400;700&display=swap">
<style>
  :root {
    --bg: #a9c8e2;
    --paper: #ffffff;
    --navy: #1c4f9c;
    --sky: #2fa6e0;
    --lime: #c8d43a;
    --magenta: #e1277a;
    --ink: #555a60;
    --brand: #1c4f9c;
  }
  html, body {
    margin: 0;
    padding: 0;
    width: 1200px;
    height: 784px;
    overflow: hidden;
    background: var(--bg);
    font-family: "Open Sans", Arial, sans-serif;
  }
  .letterhead {
    position: absolute;
    left: 345px;
    top: 32px;
    width: 509px;
    height: 720px;
    background: var(--paper);
    box-shadow: 0 6px 18px rgba(30, 60, 100, 0.25);
    overflow: hidden;
  }
  .brand {
    position: absolute;
    top: 44px;
    right: 40px;
    display: flex;
    align-items: center;
    gap: 8px;
    color: var(--brand);
    font-weight: 700;
    font-size: 22px;
    letter-spacing: -0.3px;
  }
  .brand-dot {
    width: 14px;
    height: 14px;
    border-radius: 50%;
    background: var(--brand);
  }
  .contact-line {
    position: absolute;
    left: 22px;
    bottom: 58px;
    display: flex;
    gap: 12px;
    font-size: 7.5px;
    color: var(--ink);
    white-space: nowrap;
  }
  .contact-item {
    display: flex;
    align-items: center;
    gap: 3px;
  }
  .contact-icon {
    width: 7px;
    height: 7px;
  }
  .footer-art {
    position: absolute;
    left: 0;
    bottom: 0;
    width: 509px;
    height: 52px;
  }
  .web-address {
    position: absolute;
    right: 16px;
    bottom: 12px;
    color: #fff;
    font-weight: 700;
    font-size: 11px;
    line-height: 14px;
    white-space: nowrap;
  }
</style>
</head>
<body>
  <main class="letterhead">
    <div class="brand">
      <span>harlow digital</span>
      <span class="brand-dot"></span>
    </div>

    <div class="contact-line">
      <span class="contact-item">
        <svg class="contact-icon" viewBox="0 0 10 10"><circle cx="5" cy="5" r="5" fill="#2fa6e0"/><path d="M5 2a2 2 0 0 1 2 2c0 1.5-2 4-2 4S3 5.5 3 4a2 2 0 0 1 2-2z" fill="#fff"/></svg>
        00 Elm Street East, 0th Floor, example, example N2G 4W1
      </span>
      <span class="contact-item">
        <svg class="contact-icon" viewBox="0 0 10 10"><circle cx="5" cy="5" r="5" fill="#2fa6e0"/><rect x="3.5" y="2.5" width="3" height="5" rx="0.6" fill="#fff"/></svg>
        000-000-0000
      </span>
      <span class="contact-item">
        <svg class="contact-icon" viewBox="0 0 10 10"><circle cx="5" cy="5" r="5" fill="#2fa6e0"/><rect x="2.5" y="3" width="5" height="4" fill="#fff"/></svg>
        000-000-0000
      </span>
      <span class="contact-item">
        <svg class="contact-icon" viewBox="0 0 10 10"><circle cx="5" cy="5" r="5" fill="#2fa6e0"/><path d="M2.5 3.5h5v3.5h-5z M2.5 3.5l2.5 2 2.5-2" fill="#fff" stroke="#2fa6e0" stroke-width="0.5"/></svg>
        info@harlowdigital.com
      </span>
    </div>

    <svg class="footer-art" viewBox="0 0 509 52" aria-hidden="true">
      <defs>
        <linearGradient id="tabFill" x1="0" y1="0" x2="1" y2="0">
          <stop offset="0" stop-color="#1c4f9c"/>
          <stop offset="1" stop-color="#2f8fd6"/>
        </linearGradient>
      </defs>
      <polygon points="0,30 110,30 106,34 0,34" fill="var(--sky)"/>
      <polygon points="118,30 228,30 224,34 114,34" fill="var(--lime)"/>
      <polygon points="236,30 330,30 326,34 232,34" fill="var(--magenta)"/>
      <rect x="0" y="44" width="509" height="8" fill="var(--navy)"/>
      <polygon points="350,22 509,22 509,52 338,52" fill="url(#tabFill)"/>
    </svg>
    <div class="web-address">www.harlowdigital.com</div>
  </main>
</body>
</html>
```